Fundraising campaign to raise money to purchase a pub

We are a voluntary group campaigning to stop a pub from becoming residential flats by fighting planning proposals. We are also raising money to buy or lease the pub to re-open it as a community pub.I have attached a mock idea for a flyer.We are seeking a flyer that we can use to handout.

The purpose of the flyer is to invite people to our public meeting and to complete our pub survey.

We are looking for an A5 flyer in terms of size

Target Market(s)

Local residents, investors

Industry/Entity Type

Residential

Font styles to use
Serif
Sans Serif
Decorative
Script

Requirements
Must have
• Be eyecatching. Must have a summary of the campaign. Must also have website date and time of the public meeting. Must also promote the survey and website. Must also have contact details. Must have the survey. The date and the survey should be easily spotted.
Nice to have
• A picture of the plough
Should not have
• Clip art

```html
<!DOCTYPE html>
<html lang="en">
<head>
<meta charset="utf-8">
<title>Save The Plough – Campaign Flyer</title>
<link rel="stylesheet" href="https://fonts.googleapis.com/css2?family=Arimo:wght@400;700&family=Roboto+Condensed:wght@700&display=swap">
<style>
  :root {
    --ink: #000000;
    --paper: #ffffff;
    --accent: #f6c21c;
    --badge-red: #d9262c;
    --photo-dark: #2b2824;
    --photo-mid: #5e4d3c;
    --photo-light: #9c8a76;
  }
  * { margin: 0; padding: 0; box-sizing: border-box; }
  html, body { width: 853px; height: 1200px; overflow: hidden; background: var(--paper); }
  body { font-family: "Arimo", Arial, sans-serif; }

  .flyer {
    position: relative;
    width: 853px;
    height: 1200px;
    background: var(--ink);
    color: var(--paper);
    overflow: hidden;
  }

  .pub-photo {
    position: absolute;
    left: 0; top: 0;
    width: 853px; height: 418px;
    background: linear-gradient(180deg, var(--photo-light) 0%, var(--photo-mid) 28%, var(--photo-dark) 62%, #55504a 100%);
  }

  .campaign-badge {
    position: absolute;
    top: 14px; right: 8px;
    width: 294px; height: 294px;
  }

  .summary {
    position: absolute;
    left: 34px; top: 446px;
    width: 785px;
  }
  .summary p {
    font-size: 17.5px;
    line-height: 1.36;
    margin-bottom: 19px;
  }

  .survey-callout {
    position: absolute;
    left: 34px; top: 745px;
    width: 785px;
  }
  .survey-callout h2 {
    font-family: "Roboto Condensed", "Arial Narrow", sans-serif;
    color: var(--accent);
    font-size: 33px;
    font-weight: 700;
    line-height: 1.15;
    margin-bottom: 14px;
  }
  .survey-link {
    font-size: 17px;
    font-weight: 700;
    margin-bottom: 20px;
  }
  .survey-note {
    font-size: 17px;
    line-height: 1.36;
    width: 660px;
  }
  .survey-note strong { font-weight: 700; }

  .meeting-badge {
    position: absolute;
    left: 40px; top: 930px;
    width: 165px; height: 165px;
  }

  .meeting-info {
    position: absolute;
    left: 274px; top: 940px;
    width: 540px;
  }
  .meeting-info p {
    font-size: 18px;
    line-height: 1.36;
    margin-bottom: 14px;
  }
  .meeting-info strong { font-weight: 700; }

  .site-address {
    position: absolute;
    left: 274px; top: 1108px;
    font-size: 37px;
    font-weight: 700;
  }
</style>
</head>
<body>
<main class="flyer">

  <div class="pub-photo" role="img" aria-label="Photograph of the front of The Plough pub on the high street"></div>

  <svg class="campaign-badge" viewBox="0 0 294 294" role="img" aria-label="Save The Plough">
    <circle cx="147" cy="147" r="145" fill="var(--paper)"/>
    <text x="147" y="135" text-anchor="middle" font-family="Arimo, Arial, sans-serif" font-weight="700" font-size="36" fill="var(--badge-red)">SAVE THE</text>
    <text x="147" y="180" text-anchor="middle" font-family="Arimo, Arial, sans-serif" font-weight="700" font-size="36" fill="var(--badge-red)">PLOUGH</text>
  </svg>

  <section class="summary">
    <p>The Plough, 12 Elmfield High Street, SE25 was purchased by a property developer, who proceeded to gut the pub and convert it into seven flats.</p>
    <p>The developer has tried twice to obtain planning permission and now is the subject of retrospective planning to put the pub back downstairs and in the basement. Should this not be forthcoming Northvale Council will be issue and enforcement notice to the owner.</p>
    <p>Save the Plough is a campaigning to protect the building and also raise money to lease the pub or buy the building.</p>
    <p>We want to open The Plough as a community co-op pub serving great good and wine.</p>
  </section>

  <section class="survey-callout">
    <h2>Please support our campaign by completing our survey</h2>
    <p class="survey-link">https://surveyhub.net/plough-community-survey-2024</p>
    <p class="survey-note">Paper copies of the survey are available get a friend or relative to check on <strong>www.savetheplough.co.uk</strong> for locations.</p>
  </section>

  <svg class="meeting-badge" viewBox="0 0 165 165" role="img" aria-label="Save The Plough">
    <circle cx="82.5" cy="82.5" r="80" fill="var(--paper)"/>
    <text x="82.5" y="77" text-anchor="middle" font-family="Arimo, Arial, sans-serif" font-weight="700" font-size="20" fill="var(--badge-red)">SAVE THE</text>
    <text x="82.5" y="102" text-anchor="middle" font-family="Arimo, Arial, sans-serif" font-weight="700" font-size="20" fill="var(--badge-red)">PLOUGH</text>
  </svg>

  <section class="meeting-info">
    <p>Anyone wishing to find out more about our plans to open a great pub serving fantastic food and drinks can attend our meeting 18 August at 8pm at the Harbour Light Pub, Ashgrove Road, SE25.</p>
    <p>You can contact us by email<br><strong>saveploughse25@mailbox.net</strong> or call <strong>0208 555 0142</strong></p>
  </section>

  <p class="site-address">www.savetheplough.co.uk</p>

</main>
</body>
</html>
```